Label for high-end indie coffee package

I need a label for high-end indie coffee package.

Coffee comes from Mt. Elgon, Trans-Nzoia County, Kenya. The coffee will be sold in Finland. The package as such will be semi matte black and the label will be printed out as a sticker.

Maximum measurements for the label would around 9 x 9 centimeters. It can be a square / rectangle / circle. I would like it to include influences from coffee origins (Kenya) and also demonstrate the high-end quality of the coffee with the modern twist.

The label should include the following text:

Coffee Name:
Moruvi Kelano AA
Washed & Natural

Origins:
Mt. Elgon, Trans-Nzoia County, Kenya

Growing altitude:
Altitude: 1 800 amsl

Coffee variety:
100 % Arabica

Following fields should be possible to be filled afterwards when the need occurs:
roast date
best before
roasted by

I'll be more than happy to answer any questions!

Finland. High-end customers, design coffee shops.

```html
<!DOCTYPE html>
<html lang="en">
<head>
<meta charset="utf-8">
<title>Moruvi Kelano AA – Coffee Label</title>
<link rel="stylesheet" href="https://fonts.googleapis.com/css2?family=Fira+Sans+Condensed:wght@700&family=Francois+One&family=Montserrat:wght@500;600&display=swap">
<style>
  :root {
    --navy: #24374c;
    --tan: #9a8472;
    --paper: #ffffff;
    --page: #ffffff;
  }
  html, body {
    margin: 0;
    padding: 0;
    width: 720px;
    height: 1200px;
    overflow: hidden;
    background: var(--page);
  }
  .canvas {
    position: relative;
    width: 720px;
    height: 1200px;
  }
  .label {
    position: absolute;
    left: 50px;
    top: 290px;
    width: 620px;
    height: 620px;
  }
  .arc-text {
    font-family: "Montserrat", sans-serif;
    font-weight: 500;
    font-size: 29px;
    fill: var(--navy);
    letter-spacing: 0.5px;
  }
  .coffee-name {
    font-family: "Fira Sans Condensed", sans-serif;
    font-weight: 700;
    font-size: 50px;
    fill: var(--paper);
    letter-spacing: 1px;
  }
  .process {
    font-family: "Francois One", sans-serif;
    font-size: 28px;
    fill: var(--navy);
    letter-spacing: 1px;
  }
  .variety {
    font-family: "Montserrat", sans-serif;
    font-weight: 500;
    font-size: 27px;
    fill: var(--navy);
    letter-spacing: 1px;
  }
  .field-label {
    font-family: "Montserrat", sans-serif;
    font-weight: 600;
    font-size: 16px;
    fill: var(--navy);
    letter-spacing: 0.5px;
  }
</style>
</head>
<body>
<main class="canvas">
  <svg class="label" viewBox="250 167 699 698" xmlns="http://www.w3.org/2000/svg">
    <defs>
      <path id="origin-arc" d="M 377 530 A 224 224 0 1 1 819 530"/>
      <path id="altitude-arc" d="M 370 488 A 228 228 0 0 0 826 488"/>
      <clipPath id="inner-window">
        <circle cx="598" cy="488" r="190"/>
      </clipPath>
    </defs>

    <!-- label frame -->
    <rect class="label-body" x="255" y="172" width="689" height="688" fill="var(--paper)" stroke="var(--navy)" stroke-width="4"/>
    <rect class="header-band" x="253" y="170" width="693" height="170" fill="var(--navy)"/>

    <!-- write-in fields -->
    <g class="fields" stroke="var(--navy)" stroke-width="4" fill="none">
      <line x1="255" y1="757" x2="944" y2="757"/>
      <line x1="255" y1="808" x2="944" y2="808"/>
      <line x1="597" y1="808" x2="597" y2="860"/>
    </g>
    <text class="field-label" x="275" y="792">ROAST BY</text>
    <text class="field-label" x="274" y="842">ROAST DATE</text>
    <text class="field-label" x="616" y="842">BEST BEFORE</text>

    <!-- seal -->
    <g class="seal">
      <circle cx="598" cy="488" r="286" fill="var(--paper)"/>
      <circle cx="598" cy="488" r="273" fill="var(--navy)"/>
      <circle cx="598" cy="488" r="260" fill="var(--tan)"/>
      <circle cx="598" cy="488" r="199" fill="var(--navy)"/>
      <circle cx="598" cy="488" r="190" fill="var(--paper)"/>

      <rect class="origin-scene" role="img" aria-label="Illustration of Mount Elgon peaks" x="420" y="340" width="360" height="140" fill="var(--navy)" opacity="0.85" clip-path="url(#inner-window)"/>

      <text class="arc-text"><textPath href="#origin-arc" startOffset="50%" text-anchor="middle">Mt. Elgon, Trans-Nzoia County, Kenya</textPath></text>
      <text class="arc-text"><textPath href="#altitude-arc" startOffset="50%" text-anchor="middle">Growing Altitude: 1 800 amsl</textPath></text>

      <circle class="seal-dot" cx="392" cy="594" r="9" fill="var(--navy)"/>
      <circle class="seal-dot" cx="805" cy="597" r="9" fill="var(--navy)"/>

      <path class="name-banner" d="M 330 475 L 866 475 L 866 568 L 330 568 Z" fill="var(--navy)" clip-path="url(#inner-window)"/>
      <path class="name-banner" d="M 336 475 A 273 273 0 0 1 860 475 L 860 568 A 273 273 0 0 1 336 568 Z" fill="none"/>
      <g class="name-banner-full">
        <clipPath id="outer-disc"><circle cx="598" cy="488" r="272"/></clipPath>
        <rect x="320" y="475" width="560" height="93" fill="var(--navy)" clip-path="url(#outer-disc)"/>
      </g>

      <text class="coffee-name" x="595" y="539" text-anchor="middle">MORUVI KELANO AA</text>
      <text class="process" x="603" y="597" text-anchor="middle">WASHED &amp; NATURAL</text>
      <text class="variety" x="603" y="633" text-anchor="middle">100% ARABICA</text>
    </g>
  </svg>
</main>
</body>
</html>
```